Tallow Creek Hollow Falcons Cricket Club Social Media and Logo re-design

I am seeking 14 templates (all will be similar yet slightly different - allowing us too differentiate them from others based on their use). They will be used for my local cricket club.

The following categories:
- TCHFCC Player's of the Week (Cover Page for post)
- TCHFCC Player of the Week (Plus template that matches cover to highlight each player for each team)
- TCHFCC Sponsorship Appreciation (Cover Page)
- TCHFCC Sponsorship Appreciation (4 templates that are the same, however have the following levels. 1. "Platinum Major" Sponsor. 2. "Platinum" Sponsor. 3. "Gold" Sponsor. 4. "Silver" Sponsor. 5. "Bronze" Sponsor)
- TCHFCC Around the Grounds (Cover Page)
- TCHFCC Around the Grounds (Page for each team - make similar as cover page, however needs room for a photo and small paragraph)
- TCHFCC Achievement Notice (Cover Page)
- TCHFCC Achievement Notice (Template to post attached to cover page, need room for a photo and name to be attached)
- TCHFCC Upcoming Events
- All of the above plus an attempt at a new logo. (Can either build on what we have, or come up with a new contemporary design)

Our Club Colours are Red and White, however please integrate some black or grey into the post

I am also seeking a new logo for our club to potentially implement in general and on social media. Attached below are the current logos used most of the time

Colors
EB3D1F
EC4F4E
F09395
F8D3D4
FCEDEE

Requirements
Must have
• Leave space (A rectangle or square) for us to place a picture of the players of the week. Please try and integrate the screenshots of club members attached below into the background of design covers
Nice to have
• Social Media Templates that are contemporary and allow uis to share information and display pictures on our socials that look proffessional

```html
<!DOCTYPE html>
<html lang="en">
<head>
<meta charset="utf-8">
<title>TCHFCC Player's of the Week</title>
<link rel="stylesheet" href="https://fonts.googleapis.com/css2?family=Poppins:ital,wght@0,400;0,700;1,300;1,800;1,900&family=Yellowtail&display=block">
<style>
  :root {
    --club-red: #c40006;
    --club-white: #ffffff;
  }
  html, body {
    margin: 0;
    padding: 0;
    width: 1200px;
    height: 1200px;
    overflow: hidden;
    background: var(--club-red);
  }
  .cover {
    display: block;
    width: 1200px;
    height: 1200px;
  }
  .cover__bg { fill: var(--club-red); }
  .cover__stripe, .cover__band, .cover__chevron { fill: var(--club-white); }
  .club-mark__name {
    font-family: "Poppins", sans-serif;
    font-weight: 700;
    font-size: 40px;
    fill: var(--club-white);
  }
  .club-mark__tagline {
    font-family: "Poppins", sans-serif;
    font-style: italic;
    font-weight: 300;
    font-size: 17px;
    fill: var(--club-white);
  }
  .club-initials {
    font-family: "Poppins", sans-serif;
    font-style: italic;
    font-weight: 900;
    font-size: 128px;
    fill: var(--club-red);
  }
  .headline {
    font-family: "Poppins", sans-serif;
    font-style: italic;
    font-weight: 900;
    fill: var(--club-white);
  }
  .headline--players { font-size: 84px; letter-spacing: 4px; }
  .headline--week { font-size: 104px; }
  .headline__script {
    font-family: "Yellowtail", cursive;
    font-size: 84px;
    fill: var(--club-white);
    stroke: var(--club-red);
    stroke-width: 5px;
    paint-order: stroke fill;
  }
</style>
</head>
<body>
<svg class="cover" viewBox="0 0 1080 1080" xmlns="http://www.w3.org/2000/svg" role="img" aria-label="TCHFCC Player's of the Week cover">
  <rect class="cover__bg" x="0" y="0" width="1080" height="1080"/>

  <g class="cover__stripes">
    <polygon class="cover__stripe" points="58,0 100,0 42,1080 0,1080"/>
    <polygon class="cover__stripe" points="165,0 210,0 152,1080 107,1080"/>
    <polygon class="cover__stripe" points="272,0 315,0 257,1080 214,1080"/>
    <polygon class="cover__stripe" points="378,0 410,0 352,1080 320,1080"/>
  </g>

  <polygon class="cover__band" points="384,265 1080,265 1080,415 376,415"/>

  <g class="club-mark">
    <text class="club-mark__name" x="1035" y="100" text-anchor="end">Falcons Cricket</text>
    <text class="club-mark__tagline" x="1000" y="132" text-anchor="end">where every innings counts</text>
  </g>

  <text class="club-initials" x="735" y="390" text-anchor="middle">TCHFCC</text>

  <g class="headline-group">
    <text class="headline headline--players" x="742" y="566" text-anchor="middle">PLAYER'S</text>
    <text class="headline headline--week" x="712" y="722" text-anchor="middle">WEEK</text>
    <text class="headline__script" x="722" y="636" text-anchor="middle" transform="rotate(-8 722 612)">Of The</text>
  </g>

  <g class="cover__chevrons">
    <polygon class="cover__chevron" points="680,830 715,830 770,920 715,1010 680,1010 680,955 715,920 680,885"/>
    <polygon class="cover__chevron" points="770,830 805,830 860,920 805,1010 770,1010 770,955 805,920 770,885"/>
    <polygon class="cover__chevron" points="860,830 895,830 950,920 895,1010 860,1010 860,955 895,920 860,885"/>
    <polygon class="cover__chevron" points="950,830 985,830 1040,920 985,1010 950,1010 950,955 985,920 950,885"/>
  </g>
</svg>
</body>
</html>
```